New Business Card Design Project

I'd like a business card design around the same modern style that I used on my website www.brisklanemaids.com
It's gonna be one of those round corners double-sided business cards with maybe a big logo on the front and all the info on the back of the card.

Contact Information for Business Card

Tomas Okafor
425-317-6840
www.brisklanemaids.com

www.facebook.com/BriskLaneMaidCare
www.intsgram.com/BriskLaneMaidCare

Requirements
Must have
• it needs to look elegant and modern

```html
<!DOCTYPE html>
<html lang="en">
<head>
<meta charset="UTF-8">
<title>Brisk Lane Maid Care – Business Card</title>
<link rel="stylesheet" href="https://fonts.googleapis.com/css2?family=Montserrat:wght@400;600;700&display=swap">
<style>
  :root {
    --page-bg: #e9ebee;
    --card-bg: #ffffff;
    --brand-blue: #1e9be0;
    --ink: #2b2b2b;
    --sparkle-tint: #d6ecfa;
    --card-shadow: rgba(20, 30, 45, 0.18);
  }
  * { box-sizing: border-box; margin: 0; padding: 0; }
  html, body {
    width: 1200px;
    height: 800px;
    overflow: hidden;
    background: var(--page-bg);
    font-family: "Montserrat", sans-serif;
  }
  .canvas {
    width: 1200px;
    height: 800px;
    display: flex;
    align-items: center;
    justify-content: center;
    gap: 40px;
  }
  .card {
    position: relative;
    width: 540px;
    height: 309px;
    background: var(--card-bg);
    border-radius: 18px;
    box-shadow: 0 14px 34px var(--card-shadow);
    overflow: hidden;
  }
  .card-front {
    display: flex;
    align-items: center;
    justify-content: center;
  }
  .brand-mark {
    display: flex;
    align-items: center;
    gap: 14px;
  }
  .brand-dot {
    width: 22px;
    height: 22px;
    border-radius: 50%;
    background: var(--brand-blue);
  }
  .brand-name {
    font-weight: 700;
    font-size: 38px;
    line-height: 1.05;
    color: var(--brand-blue);
    letter-spacing: -0.5px;
  }
  .card-back .sparkle-decor {
    position: absolute;
    left: 0;
    bottom: 0;
    width: 260px;
    height: 170px;
    background: radial-gradient(ellipse at 30% 80%, var(--sparkle-tint) 0%, rgba(214,236,250,0.35) 45%, rgba(255,255,255,0) 75%);
  }
  .contact-block {
    position: absolute;
    right: 34px;
    top: 96px;
    text-align: left;
  }
  .person-name {
    font-weight: 700;
    font-size: 20px;
    color: var(--brand-blue);
    margin-bottom: 12px;
    padding-left: 150px;
  }
  .contact-line {
    font-size: 12.5px;
    color: var(--ink);
    line-height: 1.75;
    white-space: nowrap;
  }
  .label {
    font-weight: 600;
    color: var(--brand-blue);
  }
  .divider { color: var(--ink); padding: 0 4px; }
  .web-host { color: var(--brand-blue); }
</style>
</head>
<body>
  <main class="canvas">
    <section class="card card-front" aria-label="Card front">
      <div class="brand-mark">
        <span class="brand-dot"></span>
        <span class="brand-name">Brisk Lane<br>Maid Care</span>
      </div>
    </section>

    <section class="card card-back" aria-label="Card back">
      <div class="sparkle-decor" role="img" aria-label="Faint light-blue sparkle decoration"></div>
      <div class="contact-block">
        <p class="person-name">Tomas Okafor</p>
        <p class="contact-line">
          <span class="label">Phone:</span> 425-317-6840<span class="divider">|</span><span class="label">Web:</span> www.<span class="web-host">brisklanemaids</span>.com
        </p>
        <p class="contact-line">
          <span class="label">Facebook:</span> BriskLaneMaidCare<span class="divider">|</span><span class="label">instagram:</span> BriskLaneMaidCare
        </p>
      </div>
    </section>
  </main>
</body>
</html>
```